Marla Q Gown Studio

My company (MarlaQ) designs and creates ladies fashion garments. I am a one person company at the moment with plans to bring on additional staff as the workload increases. At this stage I would prefer to focus on developing regional clients around Wellington, New Zealand so I can personalise the service. Expansion beyond the Wellington region is a dream in the future if all goes well with the website and the business.

I love working with people to create fashion garments for them that showcase their personalities and beauty, whatever their body type or physical appearance. I love helping my clients select the best designs, fabrics, colours and styles to look and feel the very best they can appropriate to the occasion they are dressing for. Sometimes its high-end fashion, sometimes its for daily wearing and on the odd occasion its just to be quirky and have fun with fashion. Clients typically want that special garment or outfit for special occasions like balls, weddings, racedays, reunions, concerts, anniversaries, receptions, functions and formal gatherings.

I have created a range of garments (about 12) which I would like to be showcased on the website. I can reproduce those garment showcased for clients, or I could work with the client to create a special one of a kind outfit for them, or reproduce off an existing dress design, or alter an existing outfit. have a customer focussed industry that focussing on bespoke garments rather than trying to compete with low cost mass produced ladies fashion garment.

I would like to have the prospective clients contact me by email directly from the website and work with them to design, quote, produce and tailor what they want. These fashion garments will be more expensive than off-the-rack garments readily available in shops or online. But they will be specifically tailored for the individuals. Clients will be given a quote based upon the design, type and quantity of the material used before I create the garment.

A couple of quotes in regards to my fashion design that expresses my love for creating and producing great garments for people:
- Edwin Marsh - 'You can never be overdressed or overeducated.'
- Pebbly - 'There's no need to dress like everybody else. Its much more fun to create your own.'
- Marco Dellante- 'I really want to make clothes that are feminine and help women look beautiful.'

I want to have this website hosted on a server and I want to be able to amend and update the photos and other content myself.

I like a mix of old and new sewing related art/images.

My email address and phone number should be in the contact page. They are shown in the cards below. I will upload photos of my creations soon.

Requirements
Must have
• Blog
• Services (Formal Dresses, Alterations, Buisness attire, every day wear, style consults)
Should not have
• Products

```html
<!DOCTYPE html>
<html lang="en">
<head>
<meta charset="utf-8">
<title>Marla Q Gown Studio</title>
<link href="https://fonts.googleapis.com/css2?family=Playfair+Display:wght@700&family=Montserrat:wght@600;700;800&family=Quicksand:wght@400;500&display=swap" rel="stylesheet">
<style>
:root{
  --stage:#bdbdbd;
  --white:#ffffff;
  --hero-a:#734a8e;
  --hero-b:#68589b;
  --plum:#7c5c90;
  --violet:#a26dca;
  --button:#77539a;
  --ink:#2c3340;
  --body:#6e6e78;
  --soft:#f2f2f2;
  --nav:#3d4f86;
  --star:#f4b72a;
  --tick:#5ec7e6;
}
*{margin:0;padding:0;box-sizing:border-box}
html,body{width:1200px;height:1200px;overflow:hidden;background:var(--stage)}
.stage{position:absolute;left:0;top:0;width:1500px;height:1500px;transform:scale(.8);transform-origin:0 0}
.page{position:absolute;left:258px;top:0;width:1032px;height:1454px;background:var(--white);overflow:hidden;font-family:'Quicksand',sans-serif}
.abs{position:absolute}
.nav{left:0;top:0;width:1032px;height:37px;background:var(--white);display:flex;justify-content:center;gap:19px;padding-left:10px;align-items:center;font-family:'Montserrat',sans-serif;font-size:7px;font-weight:600;color:var(--nav)}
.nav span:first-child{color:#b07c3a}
.hero{left:0;top:37px;width:1032px;height:380px;background:linear-gradient(100deg,var(--hero-a) 45%,var(--hero-b))}
.wave{left:0;width:1032px}
.eyebrow{font-family:'Montserrat',sans-serif;font-weight:700;font-size:7.5px;letter-spacing:.6px}
.hero-eyebrow{left:249px;top:114px;color:var(--white)}
.hero-title{left:249px;top:153px;width:260px;font-family:'Playfair Display',serif;font-size:32px;line-height:32px;color:var(--white);letter-spacing:-.8px}
.hero-text{left:249px;top:279px;width:230px;font-size:8.5px;line-height:14px;color:#8d7aa0}
.mock-back{left:646px;top:125px;width:173px;height:288px;background:linear-gradient(180deg,#d9d9db 0 60%,#9fe9d7 60%);}
.mock-front{left:576px;top:197px;width:139px;height:216px;background:linear-gradient(180deg,#f4f4f4,#e6e6e8);box-shadow:0 4px 14px rgba(0,0,0,.18)}
.video{left:249px;top:494px;width:285px;height:198px;background:linear-gradient(160deg,#f1f1f1,#dedcd8 70%,#c9c3b4)}
.play{left:366px;top:569px}
.video-eyebrow{left:554px;top:491px;color:var(--ink);font-weight:600;letter-spacing:1.4px;font-size:7px}
.stars{left:553px;top:508px;color:var(--star);font-size:14px;letter-spacing:2px}
.h2{font-family:'Playfair Display',serif;color:var(--ink);letter-spacing:-.5px}
.video-title{left:554px;top:533px;width:270px;font-size:23px;line-height:27px}
.p{font-size:8.5px;line-height:14px;color:var(--body)}
.video-text{left:554px;top:616px;width:260px}
.steps{left:0;top:702px;width:1032px;height:520px;background:var(--soft)}
.card{background:var(--white)}
.step1{left:249px;top:710px;width:285px;height:173px;padding:44px 20px 0}
.step2{left:534px;top:933px;width:285px;height:198px;padding:44px 20px 0}
.step-title{font-size:15px;margin-bottom:14px;letter-spacing:0}
.btn{display:inline-block;margin-top:14px;width:130px;height:25px;line-height:25px;text-align:center;background:var(--button);color:var(--white);font-family:'Montserrat',sans-serif;font-weight:700;font-size:6.5px;letter-spacing:.8px}
.circle{width:140px;height:140px;border-radius:50%;background:var(--violet);display:flex;align-items:center;justify-content:center}
.c1{left:606px;top:726px}
.c2{left:321px;top:962px}
.features-eyebrow{left:258px;top:1308px;color:var(--white);letter-spacing:.8px;font-size:7px}
.features-title{left:258px;top:1325px;font-size:23px;color:var(--white);letter-spacing:-.8px}
.list{left:258px;top:1370px;width:266px;list-style:none}
.list li{height:22px;border-bottom:1px solid rgba(255,255,255,.45);font-size:8.5px;color:#9b7cb0;padding-top:4px}
.list li:last-child{border-bottom:none}
.list li::before{content:"\2714";color:var(--tick);font-size:8px;margin-right:3px}
.growth{left:526px;top:1320px;width:300px;text-align:center;color:var(--white)}
.growth-title{font-family:'Playfair Display',serif;font-size:21px;letter-spacing:-.6px}
.growth-number{font-family:'Montserrat',sans-serif;font-weight:800;font-size:78px;line-height:80px;margin-top:6px;letter-spacing:-2px}
.growth-label{font-family:'Montserrat',sans-serif;font-weight:700;font-size:7px;margin-top:2px}
</style>
</head>
<body>
<div class="stage">
  <div class="page">
    <nav class="nav abs"><span>Home</span><span>About us</span><span>Blog</span><span>Request Quote</span><span>Contact us</span></nav>

    <section class="hero abs"></section>
    <svg class="wave abs" style="top:355px" width="1032" height="70" viewBox="0 0 1032 70" aria-hidden="true">
      <path d="M0 7 C250 25 420 48 560 53 C720 58 880 45 1032 38 L1032 70 L0 70 Z" fill="#fff"/>
    </svg>
    <div class="eyebrow hero-eyebrow abs">MARLA Q</div>
    <h1 class="hero-title abs">A Garment Specially Made For You</h1>
    <p class="hero-text abs">Crest is a single landing page template for Pagewright Layout Builder. Free to download and use on any project, and share to your circles.</p>
    <div class="mock-back abs" role="img" aria-label="App screen showing monthly follower statistics"></div>
    <div class="mock-front abs" role="img" aria-label="App screen showing a client profile card"></div>

    <div class="video abs" role="img" aria-label="Photo of a woman working at a white desk"></div>
    <svg class="play abs" width="50" height="50" viewBox="0 0 50 50" aria-hidden="true">
      <circle cx="25" cy="25" r="22" fill="none" stroke="#fff" stroke-width="2.5"/>
      <path d="M20 17 L33 25 L20 33 Z" fill="#fff"/>
    </svg>
    <div class="eyebrow video-eyebrow abs">WHATCH OUR SAMPLE VIDEO</div>
    <div class="stars abs">★★★★★</div>
    <h2 class="h2 video-title abs">A Video Presentation or a client thoughts</h2>
    <p class="p video-text abs">I am Jane Doe. I'm a client of Marla Q Company and I am really happy with their services. I catch a lot more attention since I started to listen to Marla suggestions.</p>

    <section class="steps abs"></section>
    <article class="card step1 abs">
      <h3 class="h2 step-title">Step 1 title</h3>
      <p class="p">We will put step description here. Lorem ipsum dolor sit amet, consectetur adipiscing elit. Ut elit tellus, luctus nec ullamcorper mattis, pulvinar dapibus leo.</p>
    </article>
    <div class="circle c1 abs">
      <svg width="64" height="54" viewBox="0 0 64 54" fill="none" stroke="#fff" stroke-width="1.5" aria-hidden="true">
        <rect x="2" y="2" width="56" height="36" rx="1"/><line x1="2" y1="30" x2="58" y2="30"/>
        <line x1="10" y1="9" x2="40" y2="9"/><line x1="10" y1="14" x2="48" y2="14"/><line x1="10" y1="19" x2="48" y2="19"/><line x1="10" y1="24" x2="44" y2="24"/>
        <line x1="26" y1="38" x2="26" y2="48"/><line x1="34" y1="38" x2="34" y2="48"/><line x1="18" y1="48" x2="42" y2="48"/>
        <rect x="50" y="28" width="12" height="22" rx="2" fill="#a26dca"/><line x1="54" y1="46" x2="58" y2="46"/>
      </svg>
    </div>
    <div class="circle c2 abs">
      <svg width="38" height="52" viewBox="0 0 38 52" fill="none" stroke="#fff" stroke-width="1.8" aria-hidden="true">
        <line x1="2" y1="2" x2="36" y2="2"/><line x1="2" y1="50" x2="36" y2="50"/>
        <path d="M6 6 L6 12 C6 18 19 22 19 26 C19 30 6 34 6 40 L6 46 L32 46 L32 40 C32 34 19 30 19 26 C19 22 32 18 32 12 L32 6 Z"/>
        <path d="M12 42 L19 36 L26 42 Z" fill="#fff"/>
      </svg>
    </div>
    <article class="card step2 abs">
      <h3 class="h2 step-title">Step 2 title</h3>
      <p class="p">We will put step description here.. Lorem ipsum dolor sit amet, consectetur adipiscing elit. Ut elit tellus, luctus nec ullamcorper mattis, pulvinar dapibus leo.</p>
      <span class="btn">A BUTTON IF NEEDED</span>
    </article>

    <svg class="wave abs" style="top:1150px" width="1032" height="304" viewBox="0 0 1032 304" aria-hidden="true">
      <path d="M0 38 C150 58 300 70 420 67 C640 62 860 28 1032 1 L1032 304 L0 304 Z" fill="#7c5c90"/>
    </svg>
    <div class="eyebrow features-eyebrow abs">A SECTION TO HIGHLIGHT MORE FEATURES</div>
    <h2 class="h2 features-title abs">Happy Customers</h2>
    <ul class="list abs">
      <li>Easy to use</li>
      <li>Fast process steps</li>
      <li>Different for every person</li>
      <li>Exclusive agent work with each client</li>
    </ul>
    <div class="growth abs">
      <div class="growth-title">We are growing</div>
      <div class="growth-number">363%</div>
      <div class="growth-label">MORE CLIENTS THIS YEAR</div>
    </div>
  </div>
</div>
</body>
</html>
```